Weight Loss Challenge Social Media Graphics

Create 6-7 individual social media graphics (square size) to encourage folks to join our weight loss challenge. For the color scheme of the graphics, use the color palette attached

Note: each graphic can contain any of the stock photography attached or just the single picture of me (brown shirt) but a few should be ONLY the text
For some graphics we can say: JOIN US!
For some graphics, use only TEXT based

primarily women who want to get healthy

health and weight loss

• The largest text should be: Bright Body Reset

```html
<!DOCTYPE html>
<html lang="en">
<head>
<meta charset="utf-8">
<title>Bright Body Reset – 28 Glow Challenge</title>
<link rel="stylesheet" href="https://fonts.googleapis.com/css2?family=Anton&family=Inter:wght@300;400;800;900&family=Playfair+Display:wght@900&display=swap">
<style>
  :root {
    --mauve: #ad8a87;
    --blush: #d6b8b0;
    --cream: #fbe6c4;
    --cocoa: #6b4530;
    --plum: #4a2424;
    --caramel: #8b5a3c;
    --ink: #0a0a0a;
    --white: #ffffff;
  }
  html, body {
    margin: 0;
    padding: 0;
    overflow: hidden;
    background: var(--blush);
  }
  .post {
    position: relative;
    width: 1200px;
    height: 1200px;
    overflow: hidden;
    background: var(--blush);
    font-family: "Inter", Arial, sans-serif;
  }
  .post__panel {
    position: absolute;
    left: 0;
    top: 0;
    width: 480px;
    height: 1200px;
    background: var(--mauve);
  }
  .challenge-label {
    position: absolute;
    right: 753px;
    top: 42px;
    margin: 0;
    text-align: right;
    font-size: 50px;
    line-height: 1.02;
    font-weight: 300;
    color: var(--cream);
    letter-spacing: 0.5px;
  }
  .challenge-label__number {
    font-weight: 800;
    color: var(--white);
  }
  .title {
    position: absolute;
    left: 0;
    top: 160px;
    width: 1200px;
    margin: 0;
    text-align: center;
  }
  .title__line {
    display: block;
  }
  .title__serif {
    font-family: "Playfair Display", Georgia, serif;
    font-weight: 900;
    font-size: 112px;
    line-height: 1;
    color: var(--cocoa);
    text-shadow: 2px 2px 0 var(--cream);
    letter-spacing: -1px;
  }
  .title__bold {
    font-family: "Inter", Arial, sans-serif;
    font-weight: 900;
    font-size: 150px;
    line-height: 1;
    color: var(--ink);
    letter-spacing: -4px;
    margin-top: 2px;
  }
  .photo-frame {
    position: absolute;
    left: 81px;
    top: 422px;
    width: 941px;
    height: 559px;
    background: linear-gradient(to right, var(--blush) 0 399px, var(--mauve) 399px 100%);
  }
  .photo {
    position: absolute;
    left: 19px;
    top: 19px;
    width: 903px;
    height: 521px;
    background: radial-gradient(ellipse at 50% 45%, #b68a6c 0%, #a57b5e 55%, #8f6a50 100%);
  }
  .headline {
    position: absolute;
    left: 81px;
    top: 996px;
    margin: 0;
    font-family: "Anton", Impact, sans-serif;
    font-size: 64px;
    line-height: 1;
    color: var(--plum);
    letter-spacing: 0;
    text-transform: uppercase;
    white-space: nowrap;
  }
  .headline__accent {
    color: var(--caramel);
  }
  .start-date {
    position: absolute;
    left: 81px;
    top: 1078px;
    margin: 0;
    font-size: 37px;
    font-weight: 400;
    color: var(--ink);
  }
  .join-button {
    position: absolute;
    left: 778px;
    top: 1083px;
    width: 422px;
    height: 84px;
    border-radius: 42px 0 0 42px;
    background: var(--mauve);
    display: flex;
    align-items: center;
    padding-left: 40px;
    box-sizing: border-box;
    font-size: 35px;
    font-weight: 400;
    color: var(--white);
    text-decoration: none;
    text-shadow: 1px 1px 2px rgba(0,0,0,0.6);
  }
</style>
</head>
<body>
  <main class="post">
    <div class="post__panel"></div>

    <p class="challenge-label"><span class="challenge-label__number">28</span> GLOW<br>CHALLENGE</p>

    <h1 class="title">
      <span class="title__line title__serif">BRIGHT BODY</span>
      <span class="title__line title__bold">RESET</span>
    </h1>

    <div class="photo-frame">
      <div class="photo" role="img" aria-label="Photo of five smiling women in black and white sportswear standing close together against a tan backdrop"></div>
    </div>

    <p class="headline">Lose up to 20 pounds in <span class="headline__accent">6 weeks!</span></p>
    <p class="start-date">Begins Monday, Jan 6th</p>

    <a class="join-button" href="#">JOIN US! →</a>
  </main>
</body>
</html>
```